July 15 Raffle Fundraiser to raise $2000

Fundraiser for the family to travel to Halifax NB and support athlete Corvel Ashbury.
Travel dates: July 16-23,2023

Raffling off three prizes
1) $150.00 Firewood
2) $375.00 Red Safe
3) $300.00 Secure Latch and door knob
4) 20 pieces of frozen coho sockeye

Tickets are
$2.00 each
$5.00 for three

Draw Date: July 15,2023 @11:00am

Please help us raise $2000.00
To alleviate travelling and meal costs
ETransfer: ashburyfundraiser482@plimvex.com

I have included the pervious flyer we used
Information on there as well
And please try keep same Color scheme

Thanks

Target Market(s)

Athlete supporters

Colors

Designer to choose colors to be used in the design.

Requirements
Must have
• Pictures of the raffle items , with exception of the fish there no picture of fish
Nice to have
• Pictures of the athlete in a minimal way. Similar to the colours and design of previous flyer to stay consistent. But fine if it is different.

```html
<!DOCTYPE html>
<html lang="en">
<head>
<meta charset="utf-8">
<title>Raffle Fundraiser Flyer</title>
<link href="https://fonts.googleapis.com/css2?family=Poppins:wght@400;500;600;700;800&family=Oswald:wght@500;600;700&display=swap" rel="stylesheet">
<style>
  :root {
    --blue: #1b5cb9;
    --blue-dark: #134a9c;
    --yellow: #f3cc16;
    --ink: #1e2130;
    --white: #ffffff;
    --backdrop: #7a746d;
    --court: #c9a57c;
    --wall: #8fb4c9;
  }
  * { box-sizing: border-box; margin: 0; padding: 0; }
  html, body { width: 1200px; height: 1060px; overflow: hidden; }
  body { background: var(--backdrop); font-family: 'Poppins', sans-serif; color: var(--ink); }

  .flyer {
    position: absolute; left: 230px; top: 20px;
    width: 740px; height: 1020px;
    background: var(--white); overflow: hidden;
    box-shadow: 0 12px 30px rgba(0,0,0,.35);
  }
  .hero-shapes { position: absolute; left: 0; top: 0; }
  .abs { position: absolute; }

  /* headline block */
  .headline { left: 34px; top: 40px; color: var(--white); }
  .headline .title { font-weight: 800; font-size: 50px; line-height: 1; color: var(--yellow); letter-spacing: .5px; }
  .headline .lead { font-weight: 700; font-size: 19px; margin-top: 4px; }
  .headline .city { display: flex; align-items: center; gap: 10px; margin-top: 4px; }
  .headline .city span { font-family: 'Oswald', sans-serif; font-weight: 600; font-size: 58px; line-height: 1.05; color: var(--yellow); }
  .headline .support { font-weight: 500; font-size: 18px; margin-top: 4px; }
  .headline .athlete { font-weight: 700; font-size: 31px; color: var(--yellow); line-height: 1.2; }

  /* travel dates */
  .dates { left: 44px; top: 300px; display: grid; grid-template-columns: auto auto; column-gap: 10px; align-items: end; }
  .dates .label { font-family: 'Oswald', sans-serif; font-weight: 500; font-size: 34px; line-height: 1; }
  .dates .days, .dates .year { font-family: 'Poppins', sans-serif; font-weight: 800; font-size: 56px; line-height: 1; }
  .dates .month { font-family: 'Poppins', sans-serif; font-weight: 800; font-size: 76px; line-height: .95; color: var(--blue); }

  /* gallery */
  .gallery { left: 40px; top: 462px; width: 660px; display: flex; gap: 8px; }
  .gallery .shot { flex: 1; height: 120px; border: 4px solid var(--yellow); background: linear-gradient(180deg, var(--wall) 0%, var(--wall) 55%, var(--court) 56%, #b08a60 100%); }
  .gallery .shot.jersey { background: linear-gradient(180deg, #8a7a6a, #d9d2c6); }

  /* raffle */
  .raffle { left: 40px; top: 628px; width: 660px; height: 172px; border: 3px solid var(--blue); }
  .raffle-banner {
    position: absolute; left: 120px; top: -24px; height: 40px; padding: 0 34px;
    background: var(--blue); color: var(--yellow); font-weight: 700; font-size: 22px;
    display: flex; align-items: center; clip-path: polygon(4% 0, 100% 0, 96% 100%, 0 100%);
  }
  .prizes { display: flex; height: 100%; align-items: center; padding: 14px 10px 0; }
  .prize { flex: 1; display: flex; justify-content: center; border-right: 1px solid #ddd; height: 126px; align-items: center; }
  .prize-disc {
    position: relative; width: 116px; height: 116px; border-radius: 50%;
    border: 7px solid var(--yellow); color: var(--white); text-align: center;
    display: flex; flex-direction: column; justify-content: center; align-items: center;
  }
  .prize-disc.wood { background: radial-gradient(circle, #7a5a3c, #3b2a1c); }
  .prize-disc.safe { background: radial-gradient(circle, #5a2020, #161616); }
  .prize-disc.latch { background: radial-gradient(circle, #4a4a4a, #1a1a1a); }
  .prize-disc .num {
    position: absolute; top: -14px; left: 50%; transform: translateX(-50%);
    width: 24px; height: 24px; border-radius: 50%; background: var(--blue); border: 2px solid var(--white);
    font-size: 12px; font-weight: 700; display: flex; align-items: center; justify-content: center;
  }
  .prize-disc .price { font-weight: 800; font-size: 24px; line-height: 1; }
  .prize-disc .price sup { font-size: 11px; }
  .prize-disc .item { font-weight: 600; font-size: 11px; line-height: 1.2; }
  .prize.fish { flex: 1.15; border-right: none; flex-direction: column; align-items: flex-start; justify-content: center; padding-left: 14px; }
  .fish .count { font-family: 'Oswald', sans-serif; font-weight: 600; font-size: 38px; color: var(--blue); line-height: 1; white-space: nowrap; }
  .fish .of { font-weight: 600; font-size: 15px; }
  .fish .kind { font-weight: 700; font-size: 18px; color: var(--yellow); line-height: 1.1; white-space: nowrap; }

  /* tickets */
  .tickets { left: 40px; top: 814px; display: flex; align-items: center; gap: 14px; }
  .tickets .word { font-family: 'Oswald', sans-serif; font-weight: 700; font-size: 58px; line-height: 1; }
  .stub { display: flex; height: 60px; }
  .stub .part { width: 124px; text-align: center; display: flex; flex-direction: column; justify-content: center; line-height: 1; }
  .stub .single { background: var(--blue); color: var(--yellow); }
  .stub .single small { color: var(--white); }
  .stub .triple { background: var(--yellow); color: var(--blue); }
  .stub .triple small { color: var(--ink); }
  .stub strong { font-size: 29px; font-weight: 800; }
  .stub small { font-size: 14px; font-weight: 600; margin-top: 2px; }
  .draw { margin-left: 10px; }
  .draw .label { color: var(--blue); font-weight: 700; font-size: 16px; line-height: 1.3; }
  .draw .row { display: flex; align-items: center; gap: 6px; font-weight: 700; font-size: 19px; line-height: 1.15; }

  /* footer */
  .partners { left: 40px; top: 902px; display: flex; align-items: center; gap: 16px; }
  .partner-name { font-weight: 800; font-size: 14px; color: var(--blue); display: flex; flex-direction: column; align-items: center; gap: 6px; }
  .partner-name i { width: 22px; height: 22px; background: var(--yellow); display: block; }
  .partner-badge { width: 52px; height: 68px; border: 3px solid var(--ink); background: #dff1fa; }
  .appeal { left: 268px; top: 898px; display: flex; align-items: center; gap: 14px; }
  .appeal .ask { font-weight: 800; font-size: 18px; line-height: 1.05; }
  .appeal .ask b { display: block; font-size: 25px; }
  .appeal .goal { font-family: 'Oswald', sans-serif; font-weight: 600; font-size: 46px; color: var(--blue); line-height: 1; white-space: nowrap; }
  .appeal .goal sup { font-size: 20px; }
  .appeal .costs .head { font-weight: 800; font-size: 14px; line-height: 1.3; }
  .appeal .costs li { list-style: none; font-size: 12px; font-weight: 600; display: flex; gap: 4px; align-items: center; line-height: 1.45; }
  .transfer { left: 300px; top: 982px; color: var(--white); font-size: 15px; display: flex; gap: 10px; align-items: center; }
  .transfer .method { color: var(--yellow); }
  .transfer .email { font-weight: 700; }
</style>
</head>
<body>
<main class="flyer">
  <svg class="hero-shapes" width="740" height="1020" viewBox="0 0 740 1020">
    <rect class="athlete-photo" x="300" y="0" width="440" height="450" fill="#b89a80" role="img" aria-label="Photo of the athlete playing basketball in a red team uniform on an indoor court"/>
    <polygon points="0,0 470,0 340,270 0,282" fill="var(--blue)"/>
    <line x1="470" y1="0" x2="340" y2="270" stroke="var(--yellow)" stroke-width="2" stroke-dasharray="6 4"/>
    <line x1="0" y1="278" x2="340" y2="266" stroke="var(--yellow)" stroke-width="2" stroke-dasharray="6 4"/>
    <polygon points="0,282 340,270 500,450 0,460" fill="var(--yellow)"/>
    <polygon points="256,898 740,882 740,958 240,974" fill="var(--yellow)"/>
    <polygon points="290,974 740,958 740,1020 262,1020" fill="var(--blue)"/>
    <polygon points="0,1006 250,1000 246,1020 0,1020" fill="var(--blue)"/>
  </svg>

  <header class="headline abs">
    <div class="title">FUNDRAISER</div>
    <div class="lead">FOR THE FAMILY TO TRAVEL TO</div>
    <div class="city">
      <svg width="34" height="44" viewBox="0 0 24 32" aria-hidden="true"><path d="M12 2a9 9 0 0 0-9 9c0 7 9 17 9 17s9-10 9-17a9 9 0 0 0-9-9z" fill="none" stroke="#fff" stroke-width="2.2"/><circle cx="12" cy="11" r="3.5" fill="none" stroke="#fff" stroke-width="2.2"/></svg>
      <span>HALIFAX NB</span>
    </div>
    <div class="support">AND SUPPORT ATHLETE</div>
    <div class="athlete">Corvel Ashbury</div>
  </header>

  <section class="dates abs">
    <div class="label">TRAVEL DATES</div><div class="days">16-23</div>
    <div class="month">JULY</div><div class="year">2023</div>
  </section>

  <section class="gallery abs">
    <div class="shot" role="img" aria-label="Game photo of players on an indoor court"></div>
    <div class="shot jersey" role="img" aria-label="Back view of the athlete's number 17 jersey"></div>
    <div class="shot" role="img" aria-label="Wide game photo with a referee on the court"></div>
    <div class="shot" role="img" aria-label="Athlete taking a shot near the gym wall"></div>
  </section>

  <section class="raffle abs">
    <div class="raffle-banner">RAFFLING OFF THREE PRIZES</div>
    <div class="prizes">
      <div class="prize"><div class="prize-disc wood" role="img" aria-label="Photo of stacked firewood"><span class="num">1</span><span class="price"><sup>$</sup>150.<sup>00</sup></span><span class="item">Firewood</span></div></div>
      <div class="prize"><div class="prize-disc safe" role="img" aria-label="Photo of a red safe"><span class="num">2</span><span class="price"><sup>$</sup>375.<sup>00</sup></span><span class="item">Red Safe</span></div></div>
      <div class="prize"><div class="prize-disc latch" role="img" aria-label="Photo of a secure latch and door knob"><span class="num">3</span><span class="price"><sup>$</sup>300.<sup>00</sup></span><span class="item">Secure Latch<br>and door<br>knob</span></div></div>
      <div class="prize fish"><span class="count">20 PIECES</span><span class="of">of frozen</span><span class="kind">COHO SOCKEYE</span></div>
    </div>
  </section>

  <section class="tickets abs">
    <div class="word">TICKETS</div>
    <div class="stub">
      <div class="part single"><strong>$2.00</strong><small>each</small></div>
      <div class="part triple"><strong>$5.00</strong><small>for three</small></div>
    </div>
    <div class="draw">
      <div class="label">Draw Date</div>
      <div class="row"><svg width="15" height="15" viewBox="0 0 16 16" aria-hidden="true"><rect x="1.5" y="3" width="13" height="11.5" fill="none" stroke="#1b5cb9" stroke-width="1.5"/><line x1="1.5" y1="6.5" x2="14.5" y2="6.5" stroke="#1b5cb9" stroke-width="1.5"/></svg>JULY 15,2023</div>
      <div class="row"><svg width="15" height="15" viewBox="0 0 16 16" aria-hidden="true"><circle cx="8" cy="8" r="6.5" fill="none" stroke="#1b5cb9" stroke-width="1.5"/><path d="M8 4v4l3 2" fill="none" stroke="#1b5cb9" stroke-width="1.5"/></svg>11:00AM</div>
    </div>
  </section>

  <section class="partners abs">
    <div class="partner-name"><i></i>TEAM NORTHWIND</div>
    <div class="partner-badge" role="img" aria-label="Games event badge"></div>
  </section>

  <section class="appeal abs">
    <div class="ask">PLEASE HELP<b>US RAISE</b></div>
    <div class="goal"><sup>$</sup>2000<sup>.00</sup></div>
    <div class="costs">
      <div class="head">TO ALLEVIATE</div>
      <ul>
        <li><svg width="10" height="10" viewBox="0 0 10 10" aria-hidden="true"><circle cx="5" cy="5" r="5" fill="#1b5cb9"/><path d="M2.5 5l1.8 1.8L7.5 3.5" stroke="#fff" stroke-width="1.3" fill="none"/></svg>Travelling costs</li>
        <li><svg width="10" height="10" viewBox="0 0 10 10" aria-hidden="true"><circle cx="5" cy="5" r="5" fill="#1b5cb9"/><path d="M2.5 5l1.8 1.8L7.5 3.5" stroke="#fff" stroke-width="1.3" fill="none"/></svg>Meal costs</li>
      </ul>
    </div>
  </section>

  <footer class="transfer abs">
    <span class="method">ETransfer</span><span>|</span><span class="email">ashburyfundraiser482@plimvex.com</span>
  </footer>
</main>
</body>
</html>
```